BrightKeel Business Card Contest

We are looking for a modern business card that catches attention and is unique. Attached is the brand guide and logo files. Please note that the back side (not the side with our name and info) with be UV raise printed, so have fun with the design there. We want to include Name, Title, Phone number, email, website.

Contact Information for Business Card

Please see project description

```html
<!DOCTYPE html>
<html lang="en">
<head>
<meta charset="utf-8">
<title>BrightKeel Business Card</title>
<link rel="stylesheet" href="https://fonts.googleapis.com/css2?family=Montserrat:wght@400;500;600&display=swap">
<style>
  :root {
    --stage: #2b2c2e;
    --card: #1d1d1e;
    --ink: #ffffff;
    --accent: #1fb4e2;
    --muted: #d9d9d9;
    --faint: #2c2c2e;
  }
  * { box-sizing: border-box; margin: 0; padding: 0; }
  html, body {
    width: 1027px; height: 1200px; overflow: hidden;
    background: var(--stage);
    font-family: "Montserrat", sans-serif;
    color: var(--ink);
  }
  .canvas {
    position: relative; width: 1027px; height: 1200px;
  }
  .card {
    position: absolute; left: 84px; width: 860px; height: 491px;
    background: var(--card);
    border-bottom: 8px solid var(--accent);
    border-radius: 4px;
    box-shadow: 0 18px 40px rgba(0,0,0,.45);
    overflow: hidden;
  }
  .card--front { top: 70px; }
  .card--back { top: 640px; }

  .wordmark {
    display: flex; align-items: center; gap: 16px;
    font-weight: 600; color: var(--ink); letter-spacing: -0.5px;
  }
  .wordmark__square { background: var(--accent); flex: none; }

  .card--front .wordmark {
    position: absolute; left: 58px; top: 62px; font-size: 60px;
  }
  .card--front .wordmark__square { width: 42px; height: 42px; }

  .person { position: absolute; left: 150px; top: 210px; }
  .person__name {
    font-size: 27px; font-weight: 600; color: var(--accent);
    letter-spacing: 0.5px; text-transform: uppercase;
  }
  .person__title { font-size: 21px; font-weight: 500; margin-top: 2px; }

  .contact { position: absolute; left: 150px; top: 312px; list-style: none; }
  .contact__item {
    display: flex; align-items: center; gap: 12px;
    font-size: 21px; font-weight: 400; line-height: 34px;
  }
  .contact__icon { width: 18px; height: 18px; flex: none; }

  .address {
    position: absolute; left: 548px; top: 210px;
    padding-left: 26px; border-left: 2px solid var(--accent);
    font-size: 21px; line-height: 32px; color: var(--muted);
  }

  .card--back .wordmark {
    position: absolute; left: 50%; top: 50%;
    transform: translate(-50%, -50%);
    font-size: 84px;
  }
  .card--back .wordmark__square {
    width: 150px; height: 150px; background: none;
    border: 3px solid var(--faint);
  }
</style>
</head>
<body>
<main class="canvas">
  <section class="card card--front" aria-label="Business card front">
    <div class="wordmark"><span class="wordmark__square"></span>BrightKeel</div>

    <div class="person">
      <p class="person__name">Daniel Marsh</p>
      <p class="person__title">Manager</p>
    </div>

    <ul class="contact">
      <li class="contact__item">
        <svg class="contact__icon" viewBox="0 0 24 24" fill="none" stroke="#1fb4e2" stroke-width="2.2" stroke-linecap="round" stroke-linejoin="round"><path d="M5 3h4l2 5-2.5 1.5a11 11 0 0 0 6 6L16 13l5 2v4a2 2 0 0 1-2 2A17 17 0 0 1 3 5a2 2 0 0 1 2-2z"/></svg>
        555-014-2100
      </li>
      <li class="contact__item">
        <svg class="contact__icon" viewBox="0 0 24 24" fill="none" stroke="#1fb4e2" stroke-width="2.2" stroke-linejoin="round"><rect x="2" y="5" width="20" height="14" rx="1.5"/><path d="M2 6l10 7 10-7"/></svg>
        youremail@brightkeel.com
      </li>
      <li class="contact__item">
        <svg class="contact__icon" viewBox="0 0 24 24" fill="none" stroke="#1fb4e2" stroke-width="2"><circle cx="12" cy="12" r="10"/><path d="M2 12h20M12 2c3 3 3 17 0 20M12 2c-3 3-3 17 0 20"/></svg>
        www.yourwebsite.com
      </li>
    </ul>

    <address class="address" style="font-style:normal">
      Your Address<br>City<br>State, Zip 0000
    </address>
  </section>

  <section class="card card--back" aria-label="Business card back">
    <div class="wordmark"><span class="wordmark__square"></span>BrightKeel</div>
  </section>
</main>
</body>
</html>
```